Poster for Therapy Business

We need an illustrated poster for our massage therapy business.
Looking for a graphic or image that shows we are here to help.
May like some off the wall ideas.

We use a variety of therapies to help people with chronic neck pain, head aches etc.

This poster image needs to be supplied so it wont pixilate in large size but it will also be used for a DL flyer front.

We have logo if needed.

Thanks

Target Market(s)

Target market is people working long hours at computer, admin etc.
People in chronic pain.

Industry/Entity Type

Massage

Requirements
Must have
• Level 1, Brightmark Fitness & Wellbeing,Harlow Business Estate, 417 Feltham Rd,Alexandria, NSW 2015.
www.kvremedial.example.au
(02) 5917 6403
‘help yourself to better health’
Nice to have
• Illustrated graphic
Should not have
• Not interested in the day spa image or typical generic stuff with hands, beautiful women with hots stone etc etc.

```html
<!DOCTYPE html>
<html lang="en">
<head>
<meta charset="utf-8">
<title>Beyond Therapy – Poster</title>
<link rel="stylesheet" href="https://fonts.googleapis.com/css2?family=Oswald:wght@500&family=Roboto+Condensed:ital,wght@1,700&display=swap">
<style>
  :root {
    --olive: #9b7e47;
    --ink: #000000;
    --accent-red: #e5403c;
    --headline-white: #ffffff;
    --brand-navy: #2a2f63;
    --photo-dark: #1a1511;
    --photo-mid: #5e4b33;
    --photo-light: #c9ad80;
  }
  html, body {
    margin: 0;
    padding: 0;
    overflow: hidden;
    background: #ffffff;
  }
  .poster {
    position: relative;
    width: 1200px;
    height: 825px;
    overflow: hidden;
    background: var(--olive);
  }
  .poster__night {
    position: absolute;
    left: 0;
    top: 0;
    width: 1200px;
    height: 292px;
    background: var(--ink);
  }
  .poster__photo {
    position: absolute;
    left: 0;
    top: 0;
    width: 860px;
    height: 354px;
    background:
      radial-gradient(ellipse 38% 32% at 50% 38%, var(--photo-light) 0%, var(--photo-mid) 55%, transparent 85%),
      radial-gradient(ellipse 30% 30% at 82% 70%, var(--photo-mid) 0%, transparent 80%),
      linear-gradient(180deg, var(--photo-dark) 0%, #2b2218 70%, #3a2e20 100%);
  }
  .headline {
    position: absolute;
    right: 95px;
    top: 178px;
    margin: 0;
    color: var(--headline-white);
    font-family: "Roboto Condensed", "Arial Narrow", sans-serif;
    font-weight: 700;
    font-style: italic;
    line-height: 0.98;
    text-align: right;
    transform: scaleX(0.74);
    transform-origin: right top;
  }
  .headline__line {
    display: block;
    font-size: 164px;
    letter-spacing: -2px;
  }
  .details {
    position: absolute;
    left: 398px;
    top: 0;
    transform: translateX(-50%) scaleX(0.85);
    margin: 0;
    width: 760px;
    color: var(--accent-red);
    font-family: "Oswald", "Arial Narrow", sans-serif;
    font-weight: 500;
    text-align: center;
  }
  .details__tagline,
  .details__line {
    position: absolute;
    left: 0;
    right: 0;
    margin: 0;
    white-space: nowrap;
  }
  .details__tagline {
    top: 356px;
    font-size: 42px;
    letter-spacing: 3px;
  }
  .details__line {
    font-size: 33px;
    letter-spacing: 1px;
  }
  .details__line--venue { top: 434px; }
  .details__line--estate { top: 497px; }
  .details__line--street { top: 570px; }
  .details__line--web { top: 637px; }
  .details__line--phone { top: 698px; }
  .brand {
    position: absolute;
    right: 28px;
    bottom: 36px;
    display: flex;
    align-items: center;
    gap: 8px;
    color: var(--brand-navy);
    font-family: "Oswald", "Arial Narrow", sans-serif;
    font-weight: 500;
    font-size: 15px;
    letter-spacing: 0.5px;
  }
  .brand__dot {
    width: 14px;
    height: 14px;
    border-radius: 50%;
    background: var(--brand-navy);
  }
</style>
</head>
<body>
  <main class="poster">
    <div class="poster__night"></div>
    <div class="poster__photo" role="img" aria-label="Sepia-toned photograph of a person curled up, seen from behind, against a dark background"></div>

    <h1 class="headline">
      <span class="headline__line">Beyond</span>
      <span class="headline__line">Therapy</span>
    </h1>

    <section class="details">
      <p class="details__tagline">“HELP YOURSELF TO BETTER HEALTH”</p>
      <p class="details__line details__line--venue">Level 1, Brightmark Fitness &amp; Wellbeing,</p>
      <p class="details__line details__line--estate">Harlow Business Estate,</p>
      <p class="details__line details__line--street">417 Feltham Rd, Alexandria, NSW 2015.</p>
      <p class="details__line details__line--web">www.kvremedial.example.au</p>
      <p class="details__line details__line--phone">(02) 5917 6403</p>
    </section>

    <div class="brand">
      <span class="brand__dot"></span>
      <span class="brand__name">Kestrel Valley Therapies</span>
    </div>
  </main>
</body>
</html>
```